Womens Scarves & Accessories Homepage Design

When developing this site design please have a focus on modern, stylish design. A good example of the kind of design style the client really like can be found at www.velmora-shop.com

As fashion products are the focus here clear, appealing presentation of product images is critical.

We are after a combination of http://stg72.pravtek.com.au/index.php/ mixed in with the brief file attached.

Some hero shot images have been attached

Target Market(s)

Consumer:
Lady 30 - 50
high disposable income
updating wardrobe
enjoys the shopping experience

Industry/Entity Type

Fashion

Requirements
Must have
• premium quality and elegant products - well packaged - boutique and elegant in style

The current logo must not be changed.

The slogan "spoil the girl within" must remain the same and use the current font displayed in http://stg72.pravtek.com.au

```html
<!DOCTYPE html>
<html lang="en">
<head>
<meta charset="utf-8">
<title>Lady Amaris – Scarves &amp; Accessories</title>
<link rel="stylesheet" href="https://fonts.googleapis.com/css2?family=Didact+Gothic&display=swap">
<style>
:root{
  --page-bg:#f4f4f4;
  --panel:#ffffff;
  --pink:#f6dbe4;
  --pink-light:#fbeef2;
  --pink-line:#efc7d4;
  --ink:#1a1a1a;
  --muted:#333;
  --btn:#3a3a3a;
  --frame:#c9c9c9;
  --grid-frame:#9a9a9a;
}
*{box-sizing:border-box;margin:0;padding:0}
html,body{width:1200px;height:1038px;overflow:hidden}
body{background:var(--page-bg);font-family:"Didact Gothic",sans-serif;color:var(--ink);position:relative}
a{color:var(--ink)}
.panel{position:absolute;left:162px;top:90px;width:886px;height:946px;background:var(--panel);box-shadow:0 0 8px rgba(0,0,0,.15)}
.header{position:absolute;left:183px;top:108px;width:672px;height:102px;background:linear-gradient(var(--pink-light),var(--pink));border:1px solid var(--pink-line);border-right:none}
.brand{position:absolute;left:460px;top:26px;width:210px;text-align:center;font-size:30px;color:var(--ink)}
.brand-dot{position:absolute;left:548px;top:70px;width:14px;height:14px;border-radius:50%;background:var(--ink)}
.slogan{position:absolute;left:183px;top:176px;width:672px;text-align:center;font-size:22px;letter-spacing:1px}
.cart{position:absolute;left:855px;top:108px;width:172px;height:102px;background:var(--pink-light);border:1px solid var(--pink-line);padding:4px 0 0 20px}
.cart h2{font-weight:normal;font-size:17px;margin-left:8px}
.cart p{font-size:12.5px;line-height:18px;letter-spacing:.5px}
.cart .links{margin-top:8px;font-size:12.5px;display:flex;gap:24px}
.nav{position:absolute;left:183px;top:210px;width:844px;height:33px;background:linear-gradient(var(--pink-light),var(--pink));border:1px solid var(--pink-line);display:flex;align-items:center;font-size:12px;padding:0 8px 0 15px}
.nav span.sep{margin:0 6px;color:var(--muted)}
.nav .spacer{flex:1}
.btn{background:var(--btn);color:#fff;padding:2px 8px;border:1px solid #222;font-size:12px}
.btn + .btn{margin-left:36px}
.nav .acct{margin-left:12px;display:flex}
.main-title{position:absolute;left:183px;top:262px;width:645px;text-align:center;font-size:22px;font-weight:normal}
.intro{position:absolute;left:183px;top:302px;width:645px;font-size:11px;line-height:16px}
.category{position:absolute;top:402px;width:201px}
.category .photo{height:177px;border:1px solid var(--frame);padding:3px;background:#fff}
.category .photo div{width:100%;height:100%}
.category a{display:block;text-align:center;font-size:17px;margin-top:12px}
.section-title{position:absolute;left:193px;top:630px;font-size:18px;font-weight:normal}
.products{position:absolute;left:193px;top:661px;display:grid;grid-template-columns:repeat(5,125px);grid-auto-rows:108px;gap:3px}
.products div{border:2px solid var(--grid-frame)}
.footer{position:absolute;left:191px;top:997px;width:836px;height:29px;background:var(--pink);text-align:center;font-size:11.5px;line-height:29px;letter-spacing:1px;font-weight:bold}
.side{position:absolute;left:855px;width:172px;background:linear-gradient(#fff,var(--pink-light));border:1px solid var(--pink-line);text-align:center}
.side h3{font-weight:normal;font-size:16px}
.side p{font-size:11px;line-height:16px}
.dots{position:absolute;left:857px;width:170px;border-top:2px dotted #555}
.why{top:257px;height:120px;padding:14px 14px 0}
.why p{text-align:left;margin-top:6px}
.mail{top:408px;height:175px;padding:10px 8px 0}
.mail p{text-align:left;margin:4px 0 0 7px;font-size:11px;line-height:14px}
.mail .field{margin:10px 0 0 14px;width:150px;height:19px;border:1px solid #ccc;background:#fff;font-size:10px;color:#aaa;text-align:left;padding:3px 6px}
.mail .field + .field{margin-top:4px}
.mail a{display:block;font-size:11px;margin-top:8px;margin-left:18px}
.security{top:594px;height:152px;padding:10px 10px 0}
.security h3{line-height:16px}
.security .art{margin:8px auto 0;width:82px;height:88px;background:linear-gradient(#c7ccd3,#1f5c9a)}
.testi{top:776px;height:176px;padding:10px 10px 0}
.testi p{text-align:left;font-size:10px;line-height:13.3px;margin-top:6px;padding-left:10px}
.testi .q{font-size:22px;color:#999;line-height:10px}
.testi .by{text-align:right;font-size:10px;margin-top:4px;padding-right:20px}
.social{position:absolute;left:862px;top:961px;display:flex;gap:9px}
.social span{width:19px;height:19px;display:block;border-radius:2px}
</style>
</head>
<body>
<div class="panel"></div>

<header>
  <div class="header"></div>
  <span class="brand-dot"></span>
  <div class="brand">Lady Amaris</div>
  <div class="slogan">SPOIL THE GIRL WITHIN</div>
  <div class="cart">
    <h2>Shopping Cart</h2>
    <p>Items:&nbsp;&nbsp;0<br>Total:&nbsp;&nbsp;$0.00</p>
    <div class="links"><a href="#">View Cart</a><a href="#">Checkout</a></div>
  </div>
  <nav class="nav">
    <span>Scarves</span><span class="sep">|</span><span>Wraps &amp; Shawls</span><span class="sep">|</span><span>Costume Jewellery</span>
    <span class="spacer"></span>
    <span>About U</span><span class="sep">|</span><span>Testimonials</span><span class="sep">|</span><span>FAQ</span><span class="sep">|</span><span>Contact Us</span>
    <span class="acct"><span class="btn">Register</span><span class="btn">Login</span></span>
  </nav>
</header>

<main>
  <h1 class="main-title">Stylish, affordable fashion retailors &amp; general public</h1>
  <p class="intro">Lorem Ipsum is simply dummy text of the printing and typesetting industry. Lorem Ipsum has been the industry's standard dummy text ever since the 1500s, when an unknown printer took a galley of type and scrambled it to make a type specimen book. It has survived not only five centuries, but also the leap into electronic typesetting, remaining essentially unchanged. It was popularised in the 1960s with the release of Letraset sheets containing Lorem Ipsum passages, and more recently with desktop publishing software.</p>

  <div class="category" style="left:193px">
    <div class="photo"><div role="img" aria-label="Woman in a cream coat wearing a pink knit scarf against a brick wall" style="background:linear-gradient(135deg,#9a7b6c,#d9c6bb 60%,#c98d96)"></div></div>
    <a href="#">Scarves</a>
  </div>
  <div class="category" style="left:405px">
    <div class="photo"><div role="img" aria-label="Woman in a grey wrap and shawl at a weathered wooden doorway" style="background:linear-gradient(90deg,#3d3a35,#8b7a64 50%,#4d5a3a)"></div></div>
    <a href="#">Wraps &amp; Shawls</a>
  </div>
  <div class="category" style="left:618px">
    <div class="photo"><div role="img" aria-label="Woman in sunglasses and fur stole seated in a vintage car, wearing costume jewellery" style="background:linear-gradient(135deg,#c77b80,#2c2a2a 45%,#b79a84)"></div></div>
    <a href="#">Costume Jewelry</a>
  </div>

  <h2 class="section-title">Popular Products</h2>
  <div class="products">
    <div role="img" aria-label="Tweed handbag" style="background:linear-gradient(#f2f2f2,#777)"></div>
    <div role="img" aria-label="Purple crystal bead" style="background:radial-gradient(#c9b6e0,#4b2a7a)"></div>
    <div role="img" aria-label="Colourful bead necklaces" style="background:linear-gradient(135deg,#fff,#d98fb7 50%,#8fc2a5)"></div>
    <div role="img" aria-label="Red nail polish bottles" style="background:linear-gradient(#fff,#b3202f)"></div>
    <div role="img" aria-label="Pink lipsticks" style="background:linear-gradient(#f5f5f5,#c42a7b 45%,#222)"></div>
    <div role="img" aria-label="Makeup compacts and foundation" style="background:linear-gradient(135deg,#eee,#d7b58e)"></div>
    <div role="img" aria-label="Leopard print sunglasses" style="background:linear-gradient(#fff,#6b3b1e)"></div>
    <div role="img" aria-label="White and black jacket" style="background:linear-gradient(#ddd,#8a8a8a)"></div>
    <div role="img" aria-label="White high heel sandal" style="background:linear-gradient(#fff,#ddd)"></div>
    <div role="img" aria-label="Pale blue leather gloves" style="background:linear-gradient(#fff,#a9b8cc)"></div>
    <div role="img" aria-label="Black stockings on legs" style="background:linear-gradient(135deg,#d8343c,#111 50%,#f2d38a)"></div>
    <div role="img" aria-label="Printed tote bag" style="background:linear-gradient(#e6e6e6,#a89a99)"></div>
    <div role="img" aria-label="Floral print dress" style="background:linear-gradient(#eee,#6a7a5c 60%,#d48aa0)"></div>
    <div role="img" aria-label="Charm bracelet with colourful flowers" style="background:radial-gradient(#f3d24a,#fff 70%)"></div>
    <div role="img" aria-label="Pink crystal cuff watch" style="background:linear-gradient(135deg,#fff,#d9a6b4)"></div>
  </div>
</main>

<aside>
  <section class="side why">
    <h3>Why Lady Amaris?</h3>
    <p>Fast shipping Wide &amp; varied rangenAffordable, quality products Unique Selection Constantly Updated Stock.</p>
  </section>
  <div class="dots" style="top:392px"></div>
  <section class="side mail">
    <h3>Join Our Mailing List</h3>
    <p>Lorem Ipsum is simply dummy text of the printing</p>
    <div class="field">Email</div>
    <div class="field">Get Special Offer</div>
    <a href="#">We value your privacy</a>
  </section>
  <div class="dots" style="top:578px"></div>
  <section class="side security">
    <h3>Security &amp; Credit Card Notice</h3>
    <div class="art" role="img" aria-label="Padlock resting on a blue bank card"></div>
  </section>
  <div class="dots" style="top:762px"></div>
  <section class="side testi">
    <h3>Testimonials</h3>
    <p><span class="q">&ldquo;</span> Lorem Ipsum is simply dummy text of the printing and typesetting industry. Lorem Ipsum has been the industry's standard dummy text ever since the 1500s, when an unknown printer took a galley.</p>
    <div class="by"><a href="#">Happy Client</a> <span class="q">&rdquo;</span></div>
  </section>
  <div class="social" aria-label="Social links">
    <span style="background:#4aa3c9"></span>
    <span style="background:#3b5a98"></span>
    <span style="background:#1d77b3"></span>
    <span style="background:#e0e0e0"></span>
    <span style="background:#d32b2b"></span>
    <span style="background:#ef8a22"></span>
  </div>
</aside>

<footer class="footer">Copyright © 2010-2011, Lady Amaris All rights reserved</footer>
</body>
</html>
```